Sale- Bundle signs

We are looking for a design to use for Permanent SALE/Bundle deal signs. We are a natural bath products company who uses all natural ingredients to create our handmade line of natural products. We love a clean, fresh look and feel. Simple eye-catching that will be a quick glance and they will know the offer.
We would like to have something simple, eye catching that will promote sales on our different products.
Dead Sea Salt Body Scrubs
large 2 for $40
small 3 for $20
Moisturizing Wash with coconut & olive oil
2 for $20
There are several more needed but we are hoping to decide on one template before making all of the signs.
Visit our website here www.bramblecovewash.com
Target Market(s)
Our store serves 70% women and the majority of our customers are 30+ years old.
Industry/Entity Type
It Company
Font styles to use
Other font styles liked:
- Century Gothic or similar

```html
<!DOCTYPE html>
<html lang="en">
<head>
<meta charset="utf-8">
<title>Bramble Cove – Moisturizing Wash Bundle Sign</title>
<link rel="stylesheet" href="https://fonts.googleapis.com/css2?family=Archivo:ital,wdth,wght@0,125,400;0,125,800;1,125,800&family=Questrial&display=swap">
<style>
  :root {
    --page: #ffffff;
    --sign-base: #f3f1ec;
    --sign-warm: #f1e6d6;
    --sign-cool: #dfeae6;
    --teal: #1b93ad;
    --teal-deep: #13879f;
    --olive: #6b8a2a;
    --white: #ffffff;
  }
  * { margin: 0; padding: 0; box-sizing: border-box; }
  html, body {
    width: 1200px; height: 1000px; overflow: hidden;
    background: var(--page);
  }
  .canvas { position: relative; width: 1200px; height: 1000px; }
  .sign {
    position: absolute; left: 35px; top: 83px;
    width: 1125px; height: 802px; overflow: hidden;
    background: var(--sign-base);
  }
  .backdrop {
    position: absolute; inset: 0;
    background:
      radial-gradient(ellipse at 22% 60%, rgba(255,255,255,0.9) 0 180px, transparent 420px),
      linear-gradient(135deg, var(--sign-cool) 0%, var(--sign-base) 40%, var(--sign-base) 60%, var(--sign-warm) 100%);
  }
  .offer-badge { position: absolute; left: 467px; top: 72px; }
  .offer-qty, .offer-price {
    position: absolute; color: var(--white); font-family: "Archivo", sans-serif;
    font-stretch: 125%; text-shadow: 2px 3px 6px rgba(0, 40, 60, 0.35);
    white-space: nowrap; transform-origin: left top;
  }
  .offer-qty {
    left: 655px; top: 166px; font-size: 56px; font-weight: 400;
    letter-spacing: 2px; transform: scaleX(1.32);
  }
  .offer-price {
    left: 515px; top: 188px; font-size: 262px; font-weight: 800;
    font-style: italic; letter-spacing: -6px; line-height: 1.2;
    transform: scaleX(1.2);
  }
  .offer-price .currency { font-size: 205px; vertical-align: 24px; margin-right: 8px; }
  .brand { position: absolute; left: 38px; top: 222px; }
  .brand-name {
    font-family: "Questrial", sans-serif; font-size: 56px; line-height: 1;
    color: var(--olive); letter-spacing: 1px;
  }
  .brand-tagline {
    font-family: "Questrial", sans-serif; font-size: 21px; color: var(--olive);
    letter-spacing: 1.5px; margin-top: 14px;
  }
  .product {
    position: absolute; left: 40px; top: 390px;
    font-family: "Archivo", sans-serif; font-stretch: 125%; color: var(--teal);
  }
  .product-lead { font-size: 56px; font-weight: 400; line-height: 66px; letter-spacing: -0.5px; }
  .product-key {
    font-size: 90px; font-weight: 800; line-height: 80px; color: var(--teal-deep);
    letter-spacing: -2px; margin-top: 12px;
    text-shadow: 2px 2px 4px rgba(0, 60, 80, 0.25);
  }
</style>
</head>
<body>
<main class="canvas">
  <section class="sign">
    <div class="backdrop" role="img" aria-label="Decorative backdrop area for soft translucent circles in yellow, blue, orange and peach"></div>

    <svg class="offer-badge" width="630" height="530" viewBox="0 0 630 530" aria-hidden="true">
      <defs>
        <radialGradient id="badgeFill" cx="0.4" cy="0.3" r="0.8">
          <stop offset="0" stop-color="#6cc0d2"/>
          <stop offset="0.6" stop-color="#45a8bf"/>
          <stop offset="1" stop-color="#2f93a9"/>
        </radialGradient>
      </defs>
      <ellipse cx="315" cy="265" rx="310" ry="262" fill="url(#badgeFill)"/>
    </svg>
    <div class="offer-qty">2 FOR</div>
    <div class="offer-price"><span class="currency">$</span>20</div>

    <div class="brand">
      <div class="brand-name">bramble cove</div>
      <div class="brand-tagline">NATURAL BATH PRODUCTS</div>
    </div>

    <div class="product">
      <div class="product-lead">MOISTURIZING<br>WASH WITH</div>
      <div class="product-key">COCONUT<br>&amp; OLIVE OIL</div>
    </div>
  </section>
</main>
</body>
</html>
```